Website visual upgrade

I am seeking expressions of interest for the updating the visuals of my website www.lunvaleplacements.example
I am basically seeking a simple,bold and visually strong graphic makeover.using existing or shortly to be modified text.

```html
<!DOCTYPE html>
<html lang="en">
<head>
<meta charset="utf-8">
<title>Lunvale Placements</title>
<link href="https://fonts.googleapis.com/css2?family=Source+Sans+3:ital,wght@0,400;0,600;1,400&display=swap" rel="stylesheet">
<style>
:root{
  --red:#d6102f;
  --red-dark:#b50d27;
  --ink:#3a3a3a;
  --muted:#555;
  --line:#cfcfcf;
  --page:#ffffff;
  --canvas:#efefef;
  --band:rgba(40,40,40,.72);
  --green:#9cf01a;
}
*{box-sizing:border-box;margin:0;padding:0}
html,body{width:1004px;height:1200px;overflow:hidden}
body{background:var(--canvas);font-family:"Source Sans 3",sans-serif;color:var(--ink);position:relative}
.page{position:absolute;left:87px;top:0;width:831px;height:1037px;background:var(--page);box-shadow:0 0 8px rgba(0,0,0,.18)}
.abs{position:absolute}
.brand{left:41px;top:40px;display:flex;align-items:center;gap:10px}
.brand-mark{width:22px;height:22px;background:var(--red)}
.brand-name{font-size:28px;font-weight:600;color:var(--red);letter-spacing:.3px}
.phone{left:618px;top:19px;display:flex;align-items:center;gap:6px;font-size:19px;color:var(--red)}
.search{left:623px;top:63px;width:187px;height:24px;border:1px solid #c9c9c9;border-radius:3px;display:flex;overflow:hidden}
.search span{flex:1;font-size:10px;color:#888;padding:5px 0 0 10px;display:flex;gap:8px}
.search b{width:34px;background:var(--red);color:#fff;font-weight:400;font-size:10px;text-align:center;line-height:24px}
.nav{left:0;top:103px;width:831px;height:40px;border-top:3px solid #f0f0f0;background:linear-gradient(#fff,#f6f6f6);display:flex;border-bottom:1px solid #eee}
.nav a{font-size:12.5px;color:#444;text-decoration:none;padding:11px 13px 0;border-right:1px solid #e4e4e4;white-space:nowrap}
.nav a:last-child{border:0}
.jobpanel{left:4px;top:146px;width:194px;height:323px;background:var(--red-dark)}
.jobhead{position:absolute;left:6px;top:6px;width:182px;height:37px;background:var(--red);color:#fff;font-size:22px;padding:3px 0 0 30px}
.jobhead::before{content:"";position:absolute;left:13px;top:18px;width:7px;height:7px;border-radius:50%;background:#fff}
.field{position:absolute;left:18px;width:158px;height:20px;background:#fff;border:1px solid #ddd;border-radius:2px;font-size:9px;font-style:italic;color:#999;padding:3px 0 0 18px}
.btn-search{position:absolute;left:74px;top:174px;width:99px;height:28px;border-radius:3px;background:linear-gradient(#444,#0c0c0c);color:#fff;font-size:13px;text-align:center;line-height:28px;border:1px solid #fff}
.alljobs{position:absolute;left:118px;top:213px;font-size:9.5px;font-style:italic;color:#fff}
.jotm{position:absolute;left:11px;top:243px;width:169px;height:67px;background:#c20f2b;color:#fff;padding:16px 0 0 27px}
.jotm p{font-size:13px}
.jotm small{display:block;font-size:11px;margin-top:5px}
.hero{left:198px;top:146px;width:633px;height:323px;background:linear-gradient(90deg,#c9d2dc 0%,#dde3ea 45%,#a9937d 75%,#d8dde3 100%)}
.heroband{position:absolute;left:0;bottom:0;width:100%;height:44px;background:var(--band);color:#fff;font-size:14px;padding:14px 0 0 25px}
.dots{position:absolute;right:14px;top:18px;display:flex;gap:4px}
.dots i{width:9px;height:9px;background:var(--red);border:1px solid #fff}
.card{top:494px;width:182px;height:230px;border:2px solid #e6e6e6;background:#8a96a4}
.card .band{position:absolute;left:0;bottom:0;width:100%;height:86px;background:var(--band);color:#fff;padding:5px 6px 0 13px}
.card h3{font-size:13px;font-weight:400}
.card p{font-size:10px;line-height:13.5px;margin-top:3px}
.card em{position:absolute;right:12px;bottom:6px;font-style:normal;font-size:9px;color:var(--green)}
.about{left:26px;top:758px;width:400px}
.about h2{font-size:17px;font-weight:400;color:var(--red);padding:0 0 3px 7px;border-bottom:1px solid var(--line);width:388px}
.about p{font-size:10.3px;line-height:15px;color:var(--muted);margin:13px 0 0 7px;width:393px}
.map{left:440px;top:799px;width:377px;height:167px;background:linear-gradient(#fafafa,#ececec);border-radius:4px}
.foot h4{font-size:15px;font-weight:400;color:#444}
.badge{left:87px;top:1083px;width:182px;height:53px;background:#fff;border:1px solid #e2e2e2;border-radius:3px}
.badge i{position:absolute;top:8px;height:36px}
.email{left:380px;top:1094px;width:208px;height:23px;background:#fff;border:1px solid #e6e6e6;font-size:9px;font-style:italic;color:#999;padding:5px 0 0 10px}
.subscribe{left:503px;top:1131px;width:86px;height:31px;background:var(--red);border-radius:3px;color:#fff;font-size:12px;font-weight:600;line-height:31px;text-align:center}
.social{left:795px;top:1076px;display:flex;gap:7px}
.social i{width:19px;height:16px;border-radius:2px}
.legal{right:87px;text-align:right;font-size:10.5px;color:#333}
</style>
</head>
<body>
<div class="page">
  <div class="abs brand"><span class="brand-mark"></span><span class="brand-name">Lunvale Placements</span></div>
  <div class="abs phone">
    <svg width="22" height="18" viewBox="0 0 22 18"><path d="M4 2c-2 1-3 3-1 7s6 8 9 8l2-2-3-3-2 1C7 12 6 10 5 8l1-2-2-4z" fill="#666"/><path d="M14 3a5 5 0 0 1 4 4M14 0a8 8 0 0 1 7 7" stroke="#666" fill="none"/></svg>
    1300 555 014
  </div>
  <div class="abs search"><span><svg width="12" height="12" viewBox="0 0 12 12"><circle cx="5" cy="5" r="3.5" stroke="#999" fill="none" stroke-width="1.5"/><path d="M8 8l3 3" stroke="#999" stroke-width="1.5"/></svg>Search</span><b>GO</b></div>

  <nav class="abs nav">
    <a>Home</a><a>Who We Are</a><a>Our Approach</a><a>What We Do</a><a>Migration Assistance</a><a>Job Seeker</a><a>Useful Links</a><a>Support</a><a>Contact Us</a>
  </nav>

  <section class="abs jobpanel">
    <div class="jobhead">Job Search</div>
    <div class="field" style="top:64px">Industry</div>
    <div class="field" style="top:102px">Location</div>
    <div class="field" style="top:133px;left:16px;padding-left:16px">Keword</div>
    <div class="btn-search">Search</div>
    <div class="alljobs">List All Jobs</div>
    <div class="jotm"><p>Job Of The Month</p><small>Client Sales Manager &#9656;</small></div>
  </section>

  <section class="abs hero" role="img" aria-label="Smiling businesswoman in front of a blurred office meeting">
    <div class="heroband">LOCAL PRESENCE, GLOBAL REACH<span class="dots"><i></i><i></i><i></i></span></div>
  </section>

  <article class="abs card" style="left:18px" role="img" aria-label="Business silhouettes before a world map">
    <div class="band"><h3>WHO WE ARE</h3><p>We are committed to providing the highest standards of service in Executive search.</p><em>View More &gt;&gt;</em></div>
  </article>
  <article class="abs card" style="left:219px;background:#dcdcdc" role="img" aria-label="Businessman pushing a giant puzzle piece">
    <div class="band"><h3>WHAT WE DO</h3><p>Accounting and Corporate Finance<br>Construction<br>Health and Allied Heath<br>Engineering</p><em>View More &gt;&gt;</em></div>
  </article>
  <article class="abs card" style="left:421px;background:#8a6a55" role="img" aria-label="Colleagues working together at a laptop">
    <div class="band"><h3>MIGRATION ASSISTANCE</h3><p>We can provide processing assis-tance to employers who are seek-ing suitably skilled</p><em>View More &gt;&gt;</em></div>
  </article>
  <article class="abs card" style="left:631px;background:#c5ccd4" role="img" aria-label="Silhouettes walking towards a desk">
    <div class="band"><h3>JOB SEEKER</h3><p>We are committed to providing the highest standards of service in Executive search.</p><em>View More &gt;&gt;</em></div>
  </article>

  <section class="abs about">
    <h2>About Us</h2>
    <p>We are committed to providing the highest standards<br>of service in Executive search and selection and the provision of Skilled trades people and allied Health professionals throughout Australia.</p>
    <p>We have offices throughout Australia, clearly adding<br>value to our clients’ strategic needs, wherever they may be.</p>
    <p>Competing organisations have access to similar Technology, Raw Materials and Human Capital.</p>
    <p>The ability to identify, attract and retain quality personnel will clearly differentiate those organisations which are successful and develop a corporate culture of excellence and innovation.</p>
  </section>
  <div class="abs map" role="img" aria-label="Map of Australia with links to overseas regions"></div>
</div>

<div class="abs foot" style="left:87px;top:1060px"><h4>We Proudly Support</h4></div>
<div class="abs badge"><i style="left:5px;width:106px;background:#f2e6ea;border-radius:3px"></i><i style="left:126px;width:39px;background:#111"></i></div>
<div class="abs foot" style="left:382px;top:1060px"><h4>Newsletter Signup</h4></div>
<div class="abs email">your email address here..</div>
<div class="abs subscribe">Subscribe &rsaquo;</div>
<div class="abs social"><i style="background:#59a9d8"></i><i style="background:#3b5b9a"></i><i style="background:#2a73a8"></i><i style="background:#3f7fd0"></i><i style="background:#f08a1c"></i></div>
<div class="abs legal" style="top:1103px">Privacy &nbsp;| &nbsp;Terms &amp; Conditions</div>
<div class="abs legal" style="top:1123px">Copyright © 2013 lunvaleplacements, All rights reserved</div>
</body>
</html>
```